Modern Yoga Studio Timetable and Flyer Design

We have a comprehensive class timetable and we are wanting to a clean modern look for our Spring timetable.

We require a double sided flyer with our class timetable included.
We would prefer an A5 size (postcard) or DL (1/3 A4).

We would like the final flyer to have.
Side A : Yoga image, logo

Fennel Stretch Hall
address: 4/71 Wexcombe Lane, Pelharton
website: fennelstretch.com.au
mobile: 0471 296 814

Side B: Clear easy to read timetable with a break down of class types and website.

We would also like to have a copy of the timetable itself as a separate jpg or pdf for use on our website to download.

Thank you.
Yours kindly,
Nell

I have attached a sample of another timetable of which I like the look and feel of, however this is just a guide. I've also attached our 'new' schedule in WORD plus uploaded our last design of the front.
Updates

Target Market(s)

Women aged 30-45

Industry/Entity Type

Health And Wellness

Font styles to use
Other font styles liked:
• Brandon Grotesque, Jenna Sue

Colors
6c459b
33a6d7
ffffff

Requirements
Must have
• A definitive colour to decipher between different class types on our timetable. Where each colour represents a different class type. Colours and layouts similar to our website design, see www.fennelstretch.com.au
Nice to have
• I've included a design of another studio whose timetable design I like. One of our own yoga images instead of a stock image.
Should not have
• No dark gridlines between the cells/boxes in the timetables. Please don't use stock yoga images.

```html
<!DOCTYPE html>
<html lang="en">
<head>
<meta charset="utf-8">
<title>Fennel Stretch Hall – Spring Timetable Flyer</title>
<link rel="stylesheet" href="https://fonts.googleapis.com/css2?family=Source+Sans+3:wght@400;600;700&family=Oswald:wght@500;600&display=swap">
<style>
  :root {
    --backdrop: #6e6e6e;
    --purple: #6c459b;
    --purple-deep: #3f2466;
    --blue: #33a6d7;
    --brand-blue: #4a78b8;
    --white: #ffffff;
    --ink: #2a2a2a;
    --head-cell: #d6d6d6;
    --empty-cell: #f0f0f0;
    --rise: #f2f08c;
    --mum: #e3e64a;
    --vinyasa: #b6a5d5;
    --slow: #a7d5ef;
    --yin: #9d9d9d;
    --pregnancy: #e7a3c8;
    --kids: #a9cc8f;
    --kids-junior: #d9ebcf;
    --flow-restore: #e8997a;
    --yin-restore: #df5a6a;
    --wellness: #fbf5b0;
  }
  * { box-sizing: border-box; margin: 0; padding: 0; }
  html, body { width: 1200px; height: 1200px; overflow: hidden; }
  body {
    background: var(--backdrop);
    font-family: "Source Sans 3", Arial, sans-serif;
    position: relative;
  }

  /* ---------- Side A ---------- */
  .flyer-front {
    position: absolute; left: 40px; top: 30px;
    width: 760px; height: 500px; overflow: hidden;
    box-shadow: 0 8px 24px rgba(0,0,0,.35);
  }
  .front-photo {
    position: absolute; inset: 0;
    background:
      radial-gradient(ellipse 90px 170px at 62% 40%, #fff9e6 0%, #ffd27a 35%, rgba(255,160,90,0) 75%),
      radial-gradient(ellipse 320px 160px at 35% 95%, #ff8a5c 0%, rgba(240,110,120,.6) 45%, rgba(0,0,0,0) 80%),
      radial-gradient(ellipse 260px 220px at 85% 55%, #c06a6a 0%, rgba(100,60,90,0) 80%),
      linear-gradient(160deg, #b9a0d8 0%, #c79ac8 30%, #b78aa6 55%, #5a3a5e 85%, #2f2138 100%);
  }
  .front-brand {
    position: absolute; left: 70px; top: 140px;
    font-family: "Source Sans 3", Arial, sans-serif;
    font-weight: 600; font-size: 44px; letter-spacing: 1px;
    color: var(--brand-blue);
  }
  .contact-panel {
    position: absolute; left: 30px; top: 250px;
    width: 370px; height: 112px;
    background: var(--purple-deep);
    padding: 14px 22px;
    color: var(--white);
  }
  .contact-line { display: flex; align-items: center; gap: 10px; }
  .contact-line svg { flex: none; }
  .contact-web { font-family: "Oswald", sans-serif; font-weight: 500; font-size: 19px; }
  .contact-phone { font-family: "Oswald", sans-serif; font-weight: 600; font-size: 38px; line-height: 1.05; }
  .contact-mail { font-family: "Oswald", sans-serif; font-weight: 500; font-size: 17px; }
  .address-band {
    position: absolute; left: 30px; top: 362px;
    width: 370px; height: 44px;
    background: linear-gradient(90deg, #5b86c6 0%, #86a6c9 60%, #9fb6c0 100%);
    color: var(--white); font-size: 12px; line-height: 1.25;
    padding: 7px 22px;
  }

  /* ---------- Side B ---------- */
  .flyer-back {
    position: absolute; left: 250px; top: 560px;
    width: 910px; height: 610px;
    background: var(--white);
    box-shadow: 0 8px 24px rgba(0,0,0,.35);
  }
  .timetable-title {
    position: absolute; left: 56px; top: 22px;
    font-weight: 700; font-size: 16px; color: var(--ink);
  }
  .timetable {
    position: absolute; left: 38px; top: 52px;
    display: grid;
    grid-template-columns: 80px repeat(7, 90px);
    column-gap: 5px; row-gap: 6px;
  }
  .timetable div {
    height: 22px; font-size: 13px; line-height: 22px;
    text-align: center; color: var(--ink); white-space: nowrap;
  }
  .timetable .day { background: var(--head-cell); font-weight: 700; }
  .timetable .time { text-align: right; padding-right: 8px; font-weight: 700; }
  .timetable .blank-corner { background: none; }
  .c { background: var(--empty-cell); }
  .rise { background: var(--rise); }
  .mum { background: var(--mum); }
  .vinyasa { background: var(--vinyasa); }
  .slow { background: var(--slow); }
  .yin { background: var(--yin); }
  .preg { background: var(--pregnancy); }
  .kids { background: var(--kids); }
  .kids-jr { background: var(--kids-junior); }
  .flowr { background: var(--flow-restore); }
  .yinr { background: var(--yin-restore); }
  .well { background: var(--wellness); font-size: 11px !important; letter-spacing: -.3px; }
  .booking-note {
    position: absolute; right: 52px; top: 478px;
    font-size: 13px; color: var(--ink);
  }
  .back-footer {
    position: absolute; left: 0; bottom: 0;
    width: 100%; height: 88px;
    background: var(--purple);
    color: var(--white);
  }
  .footer-address {
    position: absolute; left: 50px; top: 20px;
    display: flex; align-items: center; gap: 12px;
    font-size: 17px; line-height: 1.3;
  }
  .footer-contacts {
    position: absolute; right: 36px; top: 8px;
    display: flex; flex-direction: column; gap: 2px;
  }
  .footer-contacts .contact-line { gap: 10px; }
  .footer-phone { font-weight: 700; font-size: 22px; line-height: 1.05; }
  .footer-web { font-weight: 700; font-size: 18px; }
  .footer-mail { font-size: 16px; }
</style>
</head>
<body>

<section class="flyer-front">
  <div class="front-photo" role="img" aria-label="Photograph of a glowing candle flame among soft orange flowers on a violet background, with a faint mandala ornament and a dark floral vine decoration"></div>
  <div class="front-brand">Fennel Stretch Hall</div>

  <div class="contact-panel">
    <div class="contact-line contact-web">
      <svg width="14" height="14" viewBox="0 0 14 14"><circle cx="7" cy="7" r="6" fill="#7fb6ea"/><path d="M1 7h12M7 1v12M3 3.5q4 2 8 0M3 10.5q4-2 8 0" stroke="#fff" stroke-width=".9" fill="none"/></svg>
      www.fennelstretch.com.au
    </div>
    <div class="contact-line contact-phone">
      <svg width="16" height="16" viewBox="0 0 16 16"><path d="M2 6q6-4 12 0v2h-3V6.5H5V8H2z" fill="#7fb6ea"/><rect x="4" y="8.5" width="8" height="6" rx="1" fill="#7fb6ea"/></svg>
      0471 296 814
    </div>
    <div class="contact-line contact-mail">
      <svg width="16" height="14" viewBox="0 0 16 14"><path d="M1 6l7-5 7 5v7H1z" fill="#7fb6ea"/><path d="M1 6l7 4 7-4" stroke="#fff" fill="none"/></svg>
      hello@fennelstretch.com.au
    </div>
  </div>
  <div class="address-band">
    Wexcombe Market Ctr<br>4/71 Wexcombe Lane, Pelharton, WA 6031
  </div>
</section>

<section class="flyer-back">
  <h1 class="timetable-title">FENNEL STRETCH SPRING TIMETABLE</h1>

  <div class="timetable">
    <div class="blank-corner"></div>
    <div class="day">MON</div><div class="day">TUE</div><div class="day">WED</div><div class="day">THU</div><div class="day">FRI</div><div class="day">SAT</div><div class="day">SUN</div>

    <div class="time">5:45AM</div>
    <div class="c"></div><div class="rise">Rise + Shine*</div><div class="c"></div><div class="rise">Rise + Shine*</div><div class="c"></div><div class="c"></div><div class="c"></div>

    <div class="time">9:00AM</div>
    <div class="c"></div><div class="c"></div><div class="c"></div><div class="c"></div><div class="c"></div><div class="vinyasa">Vinyasa Flow</div><div class="c"></div>

    <div class="time">9:15AM</div>
    <div class="c"></div><div class="vinyasa">Vinyasa Flow</div><div class="c"></div><div class="c"></div><div class="c"></div><div class="c"></div><div class="yin">Yin</div>

    <div class="time">9:30AM</div>
    <div class="slow">Slow Flow</div><div class="c"></div><div class="c"></div><div class="vinyasa">Vinyasa Flow</div><div class="c"></div><div class="c"></div><div class="c"></div>

    <div class="time">10:30AM</div>
    <div class="c"></div><div class="c"></div><div class="c"></div><div class="c"></div><div class="c"></div><div class="preg">Pregnancy*</div><div class="c"></div>

    <div class="time">11:00AM</div>
    <div class="c"></div><div class="mum">Mum + Baby*</div><div class="c"></div><div class="mum">Mum + Baby*</div><div class="c"></div><div class="c"></div><div class="c"></div>

    <div class="time">12:15PM</div>
    <div class="c"></div><div class="c"></div><div class="c"></div><div class="preg">Pregnancy</div><div class="c"></div><div class="c"></div><div class="c"></div>

    <div class="time">4:00PM</div>
    <div class="c"></div><div class="c"></div><div class="kids">KIDS 8-12*</div><div class="kids-jr">Kids 5- 7*</div><div class="c"></div><div class="vinyasa">Vinyasa Flow</div><div class="c"></div>

    <div class="time">4:45PM</div>
    <div class="c"></div><div class="c"></div><div class="kids">Teens 12-16*</div><div class="c"></div><div class="c"></div><div class="c"></div><div class="c"></div>

    <div class="time">5:00PM</div>
    <div class="c"></div><div class="c"></div><div class="c"></div><div class="kids">Teens 12-16*</div><div class="c"></div><div class="c"></div><div class="c"></div>

    <div class="time">6:00PM</div>
    <div class="preg">Pregnancy*</div><div class="vinyasa">Vinyasa Flow</div><div class="slow">Slow Flow</div><div class="c"></div><div class="flowr">Flow+Restore</div><div class="c"></div><div class="c"></div>

    <div class="time">6:15PM</div>
    <div class="c"></div><div class="c"></div><div class="c"></div><div class="preg">Pregnancy*</div><div class="c"></div><div class="c"></div><div class="c"></div>

    <div class="time">7:30PM</div>
    <div class="vinyasa">Vinyasa Flow</div><div class="preg">Pregnancy*</div><div class="yinr">Yin + Restore</div><div class="well">Womens Wellness*</div><div class="c"></div><div class="c"></div><div class="c"></div>
  </div>

  <p class="booking-note">* bookings essential</p>

  <footer class="back-footer">
    <div class="footer-address">
      <svg width="26" height="38" viewBox="0 0 26 38"><path d="M13 1C6 1 1.5 6 1.5 12.5 1.5 21 13 31 13 31s11.5-10 11.5-18.5C24.5 6 20 1 13 1z" fill="#5bb2ea"/><circle cx="13" cy="12.5" r="4.5" fill="#6c459b"/><ellipse cx="13" cy="34" rx="9" ry="2.5" fill="none" stroke="#5bb2ea" stroke-width="1.5"/></svg>
      <div>Wexcombe Market Ctr,<br>4/71 Wexcombe Lane, Pelharton, WA 6031</div>
    </div>
    <div class="footer-contacts">
      <div class="contact-line footer-phone">
        <svg width="18" height="18" viewBox="0 0 16 16"><path d="M2 6q6-4 12 0v2h-3V6.5H5V8H2z" fill="#7fb6ea"/><rect x="4" y="8.5" width="8" height="6" rx="1" fill="#7fb6ea"/></svg>
        0471 296 814
      </div>
      <div class="contact-line footer-web">
        <svg width="18" height="18" viewBox="0 0 14 14"><circle cx="7" cy="7" r="6" fill="#7fb6ea"/><path d="M1 7h12M7 1v12M3 3.5q4 2 8 0M3 10.5q4-2 8 0" stroke="#fff" stroke-width=".9" fill="none"/></svg>
        www.fennelstretch.com.au
      </div>
      <div class="contact-line footer-mail">
        <svg width="18" height="16" viewBox="0 0 16 14"><path d="M1 6l7-5 7 5v7H1z" fill="#7fb6ea"/><path d="M1 6l7 4 7-4" stroke="#fff" fill="none"/></svg>
        hello@fennelstretch.com.au
      </div>
    </div>
  </footer>
</section>

</body>
</html>
```